BBQ Grill Tongs Logo and Packaging Design

Need fun exciting logo design and packaging for the best BBQ and Grilling tongs ever used.
Company Name is
Pruvel's Tongs
www.hearthclampco.com
Template layout for packaging is flat 5 x 8
We want the packaging to jump off the shelf in an eye catching design that uses vibrant colors and terminology such as..
NO more sore hands
Never Slips
Lifetime Guarantee
Best for Indoor and Outdoor BBQ and Cooking
Used by the BEST BBQ Grillmasters and Cooks
Reason: need some better designers
Target Market(s)
outdoor and indoor cooks, all ages people who purchase bbq supplies, cooking supplies and or bbq and grilling enthusists
Industry/Entity Type
Cooking
Requirements
Must have
- Bold Branding, bright colors
Nice to have
- http://www.tedmorlanz.com/
- http://www.lunadeverra.com/
- http://www.foxhollowcider.com/

```html
<!DOCTYPE html>
<html lang="en">
<head>
<meta charset="utf-8">
<title>Pruvel's Tongs – Packaging Front</title>
<link rel="stylesheet" href="https://fonts.googleapis.com/css2?family=Lobster&family=Bebas+Neue&display=swap">
<style>
  :root {
    --bg: #000000;
    --white: #ffffff;
    --badge-yellow: #f2d32e;
    --badge-red: #e0232a;
    --green: #8db53c;
    --blue: #1e9bd7;
    --flame-deep: #b8260a;
    --flame-mid: #f06a12;
    --flame-bright: #ffb627;
    --steel-light: #c9c9c9;
    --steel-dark: #6e6e6e;
  }
  html, body {
    margin: 0;
    padding: 0;
    width: 1200px;
    height: 787px;
    overflow: hidden;
    background: var(--bg);
  }
  .package-front {
    position: relative;
    width: 1200px;
    height: 787px;
    background: var(--bg);
    overflow: hidden;
  }
  .flames {
    position: absolute;
    left: 0;
    top: 500px;
    width: 1200px;
    height: 287px;
    background:
      radial-gradient(ellipse 60% 90% at 20% 100%, var(--flame-bright) 0%, transparent 70%),
      radial-gradient(ellipse 55% 85% at 80% 100%, var(--flame-bright) 0%, transparent 70%),
      linear-gradient(to bottom, rgba(0,0,0,0) 0%, var(--flame-deep) 35%, var(--flame-mid) 65%, var(--flame-bright) 100%);
  }
  .product-photo {
    position: absolute;
    left: 70px;
    top: 235px;
    width: 1110px;
    height: 310px;
  }
  .brand-title {
    position: absolute;
    left: 0;
    top: 18px;
    width: 1200px;
    margin: 0;
    text-align: center;
    font-family: "Lobster", cursive;
    font-weight: 400;
    font-size: 150px;
    line-height: 1.2;
    color: var(--white);
    letter-spacing: 1px;
  }
  .rating-badge {
    position: absolute;
    left: 273px;
    top: 409px;
    width: 670px;
    height: 78px;
    box-sizing: border-box;
    border: 7px solid var(--badge-yellow);
    display: flex;
    align-items: center;
    justify-content: center;
    font-family: "Bebas Neue", sans-serif;
    font-size: 54px;
    line-height: 1;
    color: var(--badge-red);
    letter-spacing: -0.5px;
    padding-top: 4px;
  }
  .benefits {
    position: absolute;
    left: 0;
    top: 522px;
    width: 1206px;
    margin: 0;
    padding: 0;
    list-style: none;
    text-align: center;
    font-family: "Bebas Neue", sans-serif;
    font-size: 40px;
    line-height: 45px;
    letter-spacing: -0.5px;
    color: var(--white);
  }
  .benefits .benefit--guarantee { color: var(--green); }
  .benefits .benefit--comfort { color: var(--blue); }
</style>
</head>
<body>
  <main class="package-front">
    <div class="flames" role="img" aria-label="Photograph of bright orange grill flames along the bottom edge"></div>

    <svg class="product-photo" viewBox="0 0 1110 310" role="img" aria-label="Photograph of stainless steel barbecue tongs with wooden grip, lying diagonally">
      <defs>
        <linearGradient id="steel" x1="0" y1="0" x2="0" y2="1">
          <stop offset="0" stop-color="var(--steel-light)" stop-opacity="0.55"/>
          <stop offset="1" stop-color="var(--steel-dark)" stop-opacity="0.35"/>
        </linearGradient>
      </defs>
      <polygon points="0,0 1040,40 1050,130 0,60" fill="url(#steel)"/>
      <polygon points="0,250 1040,70 1050,140 0,310" fill="url(#steel)"/>
    </svg>

    <h1 class="brand-title">Pruvel's Tongs</h1>

    <div class="rating-badge">#1 Rated Among Home Cooks</div>

    <ul class="benefits">
      <li class="benefit--guarantee">Life Time Guarantee</li>
      <li>Used by the Best</li>
      <li>BBQ Grill Masters and Cooks</li>
      <li class="benefit--comfort">No More Sore Hands</li>
      <li>Never Slips</li>
    </ul>
  </main>
</body>
</html>
```